" Empresa multidisciplinar, focada na reabilitação de pacientes com dor crônica, pós-operatório, reabilitação músculo esquelética em geral. Atendimento com educador físico, fisioterapeuta, médicos "

```html
<!DOCTYPE html>
<html lang="pt-BR">
<head>
<meta charset="UTF-8">
<title>MotriVita – Cartão de Consultas</title>
<link rel="stylesheet" href="https://fonts.googleapis.com/css2?family=Montserrat:wght@500;600;700;800&display=swap">
<style>
  :root {
    --navy: #252c43;
    --navy-deep: #1e2438;
    --yellow: #f6c11b;
    --white: #ffffff;
    --stage: #e6e6e6;
    --shadow: rgba(0,0,0,0.22);
  }
  * { box-sizing: border-box; margin: 0; padding: 0; }
  html, body { width: 1200px; height: 1200px; overflow: hidden; }
  body {
    background: var(--stage);
    font-family: "Montserrat", Arial, sans-serif;
    position: relative;
  }
  .card {
    position: absolute;
    top: 250px;
    width: 398px;
    height: 676px;
    border-radius: 26px;
    overflow: hidden;
    box-shadow: 0 10px 24px var(--shadow);
  }
  .card--front { left: 173px; background: var(--navy); }
  .card--back { left: 648px; background: var(--white); }
  .card__waves { position: absolute; left: 0; top: 0; width: 398px; height: 676px; }

  /* front */
  .front-brand {
    position: absolute; left: 0; right: 0; top: 200px;
    display: flex; flex-direction: column; align-items: center;
  }
  .front-brand__mark {
    width: 130px; height: 130px; border-radius: 50%;
    background: var(--yellow);
  }
  .front-brand__name {
    margin-top: 18px;
    font-size: 50px; font-weight: 700; color: var(--yellow);
    letter-spacing: 0.5px; line-height: 1;
  }
  .front-brand__tagline {
    margin-top: 14px;
    font-size: 11px; font-weight: 600; color: var(--white);
    letter-spacing: 0.6px; text-transform: uppercase;
  }

  /* back */
  .back-brand {
    position: absolute; left: 58px; top: 38px;
    display: flex; align-items: center; gap: 10px;
  }
  .back-brand__mark {
    width: 50px; height: 50px; border-radius: 50%;
    background: var(--navy);
  }
  .back-brand__name {
    font-size: 30px; font-weight: 700; color: var(--navy); line-height: 1;
  }
  .back-brand__tagline {
    display: block; margin-top: 5px;
    font-size: 6.5px; font-weight: 600; color: var(--navy);
    letter-spacing: 0.3px; text-transform: uppercase;
  }
  .schedule {
    position: absolute; left: 34px; top: 115px;
    width: 331px; height: 394px;
    background: var(--navy);
    border-radius: 10px;
    padding: 12px 14px 14px;
  }
  .schedule__title {
    text-align: center;
    font-size: 21px; font-weight: 800; color: var(--yellow);
    letter-spacing: 0.3px;
  }
  .schedule__table {
    margin-top: 4px;
    display: grid;
    grid-template-columns: repeat(3, 1fr);
    column-gap: 10px; row-gap: 6px;
  }
  .schedule__head {
    text-align: center;
    font-size: 11px; font-weight: 700; color: var(--white);
    padding: 4px 0 2px;
  }
  .schedule__cell { height: 37px; background: var(--white); border-radius: 2px; }
  .notice {
    position: absolute; left: 36px; right: 30px; top: 522px;
    font-size: 12.5px; font-weight: 600; color: var(--navy-deep);
    line-height: 1.35;
  }
</style>
</head>
<body>

  <section class="card card--front" aria-label="Frente do cartão">
    <div class="front-brand">
      <div class="front-brand__mark"></div>
      <h1 class="front-brand__name">MotriVita</h1>
      <p class="front-brand__tagline">Centro de Reabilitação Musculoesquelética</p>
    </div>
    <svg class="card__waves" viewBox="0 0 398 676" aria-hidden="true">
      <path d="M0,612 C120,560 280,548 398,566 L398,676 L0,676 Z" fill="#f6c11b"/>
      <path d="M0,636 C130,590 280,585 398,602 L398,676 L0,676 Z" fill="#ffffff"/>
      <path d="M0,646 C130,604 280,600 398,618 L398,676 L0,676 Z" fill="#252c43"/>
    </svg>
  </section>

  <section class="card card--back" aria-label="Verso do cartão">
    <div class="back-brand">
      <div class="back-brand__mark"></div>
      <div>
        <span class="back-brand__name">MotriVita</span>
        <span class="back-brand__tagline">Centro de Reabilitação Musculoesquelética</span>
      </div>
    </div>

    <div class="schedule">
      <h2 class="schedule__title">PRÓXIMAS CONSULTAS</h2>
      <div class="schedule__table">
        <div class="schedule__head">DATA</div>
        <div class="schedule__head">HORÁRIO</div>
        <div class="schedule__head">LOCAL</div>
        <div class="schedule__cell"></div><div class="schedule__cell"></div><div class="schedule__cell"></div>
        <div class="schedule__cell"></div><div class="schedule__cell"></div><div class="schedule__cell"></div>
        <div class="schedule__cell"></div><div class="schedule__cell"></div><div class="schedule__cell"></div>
        <div class="schedule__cell"></div><div class="schedule__cell"></div><div class="schedule__cell"></div>
        <div class="schedule__cell"></div><div class="schedule__cell"></div><div class="schedule__cell"></div>
        <div class="schedule__cell"></div><div class="schedule__cell"></div><div class="schedule__cell"></div>
        <div class="schedule__cell"></div><div class="schedule__cell"></div><div class="schedule__cell"></div>
      </div>
    </div>

    <p class="notice">*Importante: Caso não possa comparecer à consulta agendada, por favor, avise-nos com pelo menos 24 horas de antecedência.</p>

    <svg class="card__waves" viewBox="0 0 398 676" aria-hidden="true">
      <path d="M0,628 C130,582 280,580 398,600 L398,676 L0,676 Z" fill="#f6c11b"/>
      <path d="M0,640 C130,598 280,596 398,616 L398,676 L0,676 Z" fill="#252c43"/>
    </svg>
  </section>

</body>
</html>
```